Buch-Cover für Sonnenherz gesucht
Der Designer hat sich sehr schnell in meine Vorgaben eingearbeitet und gleichzeitig wertvolle Vorschläge zur Optimierung abgegeben. Das Ergebnis ist dadurch sogar besser geworden, als ich mir im Vorfeld ausgemalt hatte. 100% Weiterempfehlung.
Zielgruppe
Wir sind eine Firma die hochwertige Fitnessprodukte produziert und vertreibt. Unsere Zielgruppe sind gesundheitsbewusste Frauen ab Mitte 20 bis open end, die hohe Ansprüche an sich selbst stellen und sich für das Thema Selbstoptimierung interessieren.
Aufgabenstellung
Es soll ein Hardcover gestaltet werden.
Buchtitel: Sonnenherz, Untertitel: Das Erwachen der Seele
Detaillierte Beschreibung der Projektanforderungen siehe Anhang Projektbeschreibung. Darüber hinaus bin ich auch für alternative Gestaltungs-Ideen offen.
Das Design soll der Käuferin folgendes vermitteln:
- Wertigkeit
- Positivität
und sie ein bisschen träumen lassen und natürlich neugierig auf den Inhalt machen.

```html
<!DOCTYPE html>
<html lang="de">
<head>
<meta charset="utf-8">
<title>Sonnenherz – Buchumschlag</title>
<link rel="stylesheet" href="https://fonts.googleapis.com/css2?family=Bebas+Neue&family=Oswald:wght@500&family=Open+Sans:wght@400&family=Reenie+Beanie&family=Fira+Sans+Condensed:wght@300;500;600&display=swap">
<style>
  :root {
    --navy: #1c2a4e;
    --teal: #0f8a86;
    --teal-deep: #0b5e5c;
    --teal-mid: #1a7d79;
    --glow: #e9b27a;
    --rose: #d9a08e;
    --white: #ffffff;
    --frame: rgba(255,255,255,0.75);
    --script-red: #b5242b;
    --placeholder: #f9e6dc;
    --ink: #2a2a2a;
  }
  * { margin: 0; padding: 0; box-sizing: border-box; }
  html, body { width: 1200px; height: 904px; overflow: hidden; background: #ffffff; }
  .jacket { position: relative; width: 1200px; height: 904px; }

  /* Back cover */
  .back {
    position: absolute; left: 0; top: 0; width: 556px; height: 904px;
    background:
      radial-gradient(ellipse 260px 200px at 330px 170px, rgba(240,190,120,0.75), transparent 70%),
      radial-gradient(ellipse 300px 160px at 120px 120px, rgba(200,150,150,0.45), transparent 70%),
      linear-gradient(180deg, #1f3a5e 0%, #3d6d7a 18%, #5b8c82 32%, var(--teal-mid) 50%, var(--teal) 68%, var(--teal-deep) 100%);
    overflow: hidden;
  }
  .back-frame { position: absolute; left: 15px; top: 15px; right: 0; bottom: 12px; border: 1px solid var(--frame); border-right: none; }
  .back-question {
    position: absolute; left: 150px; top: 92px; width: 280px;
    font-family: "Oswald", sans-serif; font-weight: 500; font-size: 68px; line-height: 0.98;
    color: rgba(255,255,255,0.88); text-align: center; letter-spacing: -1px;
  }
  .blurb {
    position: absolute; left: 71px; top: 318px; width: 429px;
    font-family: "Open Sans", sans-serif; font-size: 14.2px; line-height: 20.2px;
    color: var(--white); text-align: justify;
  }
  .blurb p + p { margin-top: 20px; }
  .barcode-slot {
    position: absolute; left: 311px; top: 723px; width: 216px; height: 130px;
    background: var(--placeholder);
    display: flex; align-items: center; justify-content: center; text-align: center;
    font-family: "Fira Sans Condensed", sans-serif; font-weight: 600; font-size: 18px; line-height: 27px; color: var(--ink);
  }

  /* Spine */
  .spine {
    position: absolute; left: 556px; top: 0; width: 86px; height: 904px;
    background: var(--teal);
    border-left: 1px solid var(--frame); border-right: 1px solid var(--frame);
  }
  .spine-slot {
    position: absolute; left: 0; width: 84px;
    display: flex; align-items: center; justify-content: center; overflow: hidden;
  }
  .spine-slot span {
    writing-mode: vertical-rl; transform: rotate(180deg); white-space: nowrap; line-height: 1;
  }
  .spine-title { top: 198px; height: 222px; }
  .spine-title span { font-family: "Bebas Neue", sans-serif; font-size: 50px; color: var(--white); letter-spacing: 1px; }
  .spine-imprint { top: 426px; height: 62px; }
  .spine-imprint span { font-family: "Fira Sans Condensed", sans-serif; font-weight: 500; font-size: 12px; color: var(--glow); letter-spacing: 1px; }
  .spine-author { top: 495px; height: 190px; }
  .spine-author span { font-family: "Fira Sans Condensed", sans-serif; font-weight: 300; font-size: 26px; color: var(--white); letter-spacing: 0.5px; }

  /* Front cover */
  .front { position: absolute; left: 642px; top: 0; width: 558px; height: 904px; overflow: hidden; }
  .front-photo {
    position: absolute; inset: 0;
    background:
      radial-gradient(ellipse 320px 180px at 300px 360px, rgba(245,200,150,0.8), transparent 70%),
      linear-gradient(180deg, #1a2a52 0%, #2f4a6c 12%, #7c7a86 26%, var(--rose) 38%, #e8b595 48%, #9c8a78 60%, #5d5a52 72%, #3a3634 86%, #262322 100%);
  }
  .front-frame { position: absolute; left: 0; top: 15px; right: 15px; bottom: 12px; border: 1px solid var(--frame); border-left: none; }
  .imprint-rule {
    position: absolute; left: 188px; top: 78px; width: 300px;
    display: flex; align-items: center; gap: 12px;
  }
  .imprint-rule .line { flex: 1; height: 1px; background: var(--white); }
  .imprint-rule .name {
    font-family: "Fira Sans Condensed", sans-serif; font-weight: 500; font-size: 15px; color: var(--white); letter-spacing: 2px;
  }
  .front-title {
    position: absolute; left: 0; width: 543px; top: 112px; text-align: center;
    font-family: "Bebas Neue", sans-serif; font-size: 122px; line-height: 1; color: var(--white); letter-spacing: 1px;
    transform: scaleY(1.4); transform-origin: top center;
  }
  .front-subtitle {
    position: absolute; left: 0; width: 543px; top: 292px; text-align: center;
    font-family: "Reenie Beanie", cursive; font-size: 50px; line-height: 1; color: var(--script-red);
  }
  .front-author {
    position: absolute; left: 0; width: 543px; top: 822px; text-align: center;
    font-family: "Fira Sans Condensed", sans-serif; font-weight: 600; font-size: 30px; color: var(--white); letter-spacing: 2px;
    text-shadow: 0 1px 3px rgba(0,0,0,0.4);
  }
</style>
</head>
<body>
<main class="jacket">
  <section class="back">
    <div class="back-frame"></div>
    <h2 class="back-question">Was<br>zählt<br>wirklich?</h2>
    <div class="blurb">
      <p>Ich habe mich oft gefragt: Wie soll ich bloß die Liebe und Bestätigung, die mir damals in meiner Kindheit verwehrt blieben, „nachholen“? Lösungsansätze für mein Problem hatte ich in der Vergangenheit durchaus: Ich versuchte das Loch in mir mit Hilfe zur Selbsthilfe, Erfolg im Job und Konsum zu stopfen. Und meine Partner mussten auch für so einiges herhalten.</p>
      <p>Von Gott wollte ich lange nichts wissen. Schließlich hatte er es zugelassen, dass mir sehr viel Unheil in meinem Leben widerfahren ist. Und deshalb war ich echt wütend auf ihn.</p>
      <p>Heutzutage bin ich mir sicher, dass ich mit dieser Denkweise meine Lebenszeit verschwendet habe. Letzten Sommer begriff ich endlich: im Leben gilt die gleiche Gesetzmäßigkeit wie beim Autofahren. Der Rückspiegel ist so klein und die Frontscheibe so groß, weil das, was vor uns liegt, viel wichtiger ist als das, was hinter uns liegt. Aufgrund dieser Erkenntnis entschied ich mich, einen völlig neuen Weg einzuschlagen und wagte mich auf eine spannende Reise, die mein Leben für immer veränderte …</p>
    </div>
    <div class="barcode-slot">Barcode<br>Location &amp; Size<br>2” X 1.2”</div>
  </section>

  <section class="spine">
    <div class="spine-slot spine-title"><span>SONNENHERZ</span></div>
    <div class="spine-slot spine-imprint"><span>Lumenhaus</span></div>
    <div class="spine-slot spine-author"><span>Mara Feltkamp</span></div>
  </section>

  <section class="front">
    <div class="front-photo" role="img" aria-label="Foto: Frau am Steuer eines offenen Cabrios, von hinten gesehen, auf einem Feldweg in sommerlichem Abendlicht mit Lichtreflexen"></div>
    <div class="front-frame"></div>
    <div class="imprint-rule"><span class="line"></span><span class="name">Lumenhaus</span><span class="line"></span></div>
    <h1 class="front-title">SONNENHERZ</h1>
    <p class="front-subtitle">Das Erwachen der Seele</p>
    <p class="front-author">Mara Feltkamp</p>
  </section>
</main>
</body>
</html>
```